Business Card/ Email Signature Design Project

I am an Interior Designer. I need a business card that looks sophisticated stylish but simple in design. My work covers space design/ interior architecture/ furniture design/ product development & styling.

I have a very specific brief and know mostly what I want. I'm hoping to work with someone who can translate my ideas.

My branding should have a strong focus on my name, the majority of my work is referral based.
I'm keen to keep a monochromatic colour scheme: dark charcoal/ black/ white/ embossing/ silver. I'm not suggesting we use all that I've listed, they are possible ideas at this stage. I will need to be mindful of printing costs an also how I make the design work across, cards, letter heads, email logo and web design.

Theory behind images sent below;
1-Rug Image_(minus boarder) I was thinking this image could be used on the back of the card with my contact details over. I like that the lines are almost hand drawn and start to look free form. It's a subtle contrast to a more formal front of the card with my name.
2_Tomas Ferle_I really like the orientation, the proportion of font on the card, the colour and the font. I like the lower case for my name and the upper case for 'Interior Design'. Not sure if it should be 'Interior Designer or Interior Design' at this stage, was leaning towards 'Interior Design'. Was thinking the 'i' and 'd' in my surname could be the colour eg 'silver'?? We can decide on this once we see it.

Look forward to hearing from you.
Cheers,
Saskia Bremond

Printing

Saskia Bremond Interior Design

```html
<!DOCTYPE html>
<html lang="en">
<head>
<meta charset="utf-8">
<title>Saskia Bremond Interior Design – Business Card</title>
<link rel="stylesheet" href="https://fonts.googleapis.com/css2?family=Questrial&family=Gilda+Display&display=swap">
<style>
  :root {
    --backdrop: #c8cfd0;
    --rug-light: #c4c4c4;
    --rug-mid: #8d8d8d;
    --panel: #5b5b5b;
    --panel-edge: #ffffff;
    --name-ink: #e6e6e6;
    --ink: #1a1a1a;
    --rule: #555555;
    --paper: #ffffff;
  }
  * { box-sizing: border-box; margin: 0; padding: 0; }
  html, body { width: 1200px; height: 773px; overflow: hidden; }
  body { background: var(--backdrop); position: relative; }

  .card {
    position: absolute;
    top: 268px;
    width: 410px;
    height: 238px;
    overflow: hidden;
    box-shadow: 0 2px 6px rgba(0,0,0,0.18);
  }
  .card--front { left: 180px; }
  .card--back { left: 610px; background: var(--paper); }

  /* front */
  .rug-texture {
    position: absolute; inset: 0;
    background: linear-gradient(135deg, var(--rug-mid), #a2a2a2 50%, var(--rug-mid));
  }
  .name-panel {
    position: absolute;
    left: 28px; top: 20px; right: 28px; bottom: 20px;
    background: linear-gradient(160deg, #646464, var(--panel));
    border: 3px solid var(--panel-edge);
  }
  .name-block {
    position: absolute;
    left: 20px; top: 68px;
  }
  .name {
    font-family: "Questrial", sans-serif;
    font-weight: 400;
    font-size: 36px;
    line-height: 1;
    color: var(--name-ink);
  }
  .discipline {
    margin-top: 6px;
    font-family: "Questrial", sans-serif;
    font-weight: 400;
    font-size: 15px;
    letter-spacing: 2px;
    color: var(--name-ink);
  }

  /* back */
  .rug-band {
    position: absolute; left: 0; right: 0;
    background: linear-gradient(90deg, var(--rug-light), #d6d6d6 50%, var(--rug-light));
  }
  .rug-band--top { top: 0; height: 46px; }
  .rug-band--bottom { bottom: 0; height: 50px; }
  .rule {
    position: absolute; left: 0; right: 0; height: 5px; background: var(--rule);
  }
  .rule--top { top: 46px; }
  .rule--bottom { bottom: 50px; }
  .contact {
    position: absolute;
    left: 0; right: 0; top: 78px;
    text-align: center;
    font-family: "Gilda Display", serif;
    font-size: 14.5px;
    line-height: 18px;
    color: var(--ink);
    list-style: none;
  }
</style>
</head>
<body>
  <section class="card card--front" aria-label="Business card front">
    <div class="rug-texture" role="img" aria-label="Grey rug texture with free-form hand-drawn line pattern"></div>
    <div class="name-panel" role="img" aria-label="Darker grey rug texture panel">
      <div class="name-block">
        <p class="name">saskia bremond</p>
        <p class="discipline">Interior Designer</p>
      </div>
    </div>
  </section>

  <section class="card card--back" aria-label="Business card back">
    <div class="rug-band rug-band--top" role="img" aria-label="Light grey rug texture with hand-drawn line pattern"></div>
    <div class="rule rule--top"></div>
    <ul class="contact">
      <li>Address: P.O Box 214 Fairhaven VIC. 3061</li>
      <li>Email: interiors@saskiabremond.com</li>
      <li>Web: www.saskiabremond.com</li>
      <li>Mobile: 0400 555 127</li>
    </ul>
    <div class="rule rule--bottom"></div>
    <div class="rug-band rug-band--bottom" role="img" aria-label="Light grey rug texture with hand-drawn line pattern"></div>
  </section>
</body>
</html>
```